Business Card / Letterhead / Envelopes for Investment Advisor
Crest Wealth Allies
Business Card / Letterhead / Envelopes for Investment Advisor - Financial Services
Creative Brief
Professional
Dwayne Holloran
Investment Advisor
4827 Tamsworth Avenue Reading, PA 19432
610-555-0148 ext 317
dwayne@crestwa.com
www.crestwa.com

```html
<!DOCTYPE html>
<html lang="en">
<head>
<meta charset="utf-8">
<title>Crest Wealth Allies – Envelope</title>
<link rel="stylesheet" href="https://fonts.googleapis.com/css2?family=Arimo:wght@400&family=Libre+Baskerville:wght@400&display=swap">
<style>
  :root {
    --page-bg: #e6e6e8;
    --paper: #ffffff;
    --navy: #1f5597;
    --ink: #3a3a3a;
    --brand-ink: #222222;
    --window: #d9dbdd;
    --edge: #d4d4d4;
  }
  html, body {
    margin: 0;
    padding: 0;
    width: 1200px;
    height: 871px;
    overflow: hidden;
    background: var(--page-bg);
  }
  body {
    position: relative;
  }
  .envelope {
    position: absolute;
    left: 106px;
    top: 204px;
    width: 1022px;
    height: 468px;
    background: var(--paper);
    border: 1px solid var(--edge);
    box-sizing: border-box;
    overflow: hidden;
    font-family: "Arimo", Arial, sans-serif;
    color: var(--ink);
  }
  .address-window {
    position: absolute;
    left: 76px;
    top: 86px;
    width: 236px;
    height: 80px;
    background: var(--window);
    border-radius: 8px;
  }
  .brand {
    position: absolute;
    left: 556px;
    top: 48px;
    display: flex;
    align-items: center;
    gap: 18px;
  }
  .brand-square {
    width: 70px;
    height: 70px;
    background: var(--navy);
    flex: none;
  }
  .brand-name {
    font-family: "Libre Baskerville", Georgia, serif;
    font-size: 22px;
    letter-spacing: 2px;
    color: var(--brand-ink);
    white-space: nowrap;
  }
  .return-address {
    position: absolute;
    left: 74px;
    top: 212px;
    margin: 0;
    font-size: 16px;
    line-height: 20px;
    font-style: normal;
  }
  .contact-list {
    position: absolute;
    left: 74px;
    top: 274px;
    margin: 0;
    padding: 0;
    list-style: none;
    font-size: 16px;
  }
  .contact-list li {
    display: flex;
    align-items: center;
    gap: 12px;
    height: 21.5px;
  }
  .contact-list svg {
    width: 16px;
    height: 16px;
    fill: var(--navy);
    flex: none;
  }
  .base-band {
    position: absolute;
    left: 0;
    right: 0;
    bottom: 0;
    height: 42px;
    background: var(--navy);
  }
</style>
</head>
<body>
  <div class="envelope">
    <div class="address-window"></div>

    <div class="brand">
      <div class="brand-square"></div>
      <div class="brand-name">CREST WEALTH ALLIES</div>
    </div>

    <address class="return-address">4827 Tamsworth Avenue<br>Reading, PA 19432</address>

    <ul class="contact-list">
      <li>
        <svg viewBox="0 0 16 16" aria-hidden="true"><path d="M3.5 1.5l2.5 0 1 3.5-1.8 1.2a9 9 0 0 0 4.6 4.6L11 9l3.5 1v2.5c0 1-1 2-2 2C6.5 14.5 1.5 9.5 1.5 3.5c0-1 1-2 2-2z"/></svg>
        <span>610-555-0148</span>
      </li>
      <li>
        <svg viewBox="0 0 16 16" aria-hidden="true"><path d="M3.5 1.5l2.5 0 1 3.5-1.8 1.2a9 9 0 0 0 4.6 4.6L11 9l3.5 1v2.5c0 1-1 2-2 2C6.5 14.5 1.5 9.5 1.5 3.5c0-1 1-2 2-2z"/></svg>
        <span>610-555-0192</span>
      </li>
      <li>
        <svg viewBox="0 0 16 16" aria-hidden="true"><path d="M4 1h6l2 2v3H4z M1.5 6.5h13v7h-13z M4 9h2v1.5H4z M7 9h2v1.5H7z M10 9h2v1.5h-2z" fill-rule="evenodd"/></svg>
        <span>610-555-0163</span>
      </li>
      <li>
        <svg viewBox="0 0 16 16" aria-hidden="true"><path d="M1 3h14v10H1z M2.5 4.5L8 9l5.5-4.5v7h-11z" fill-rule="evenodd"/></svg>
        <span>dwayne@crestwa.com</span>
      </li>
      <li>
        <svg viewBox="0 0 16 16" aria-hidden="true"><path d="M8 1a7 7 0 1 0 0 14A7 7 0 0 0 8 1zm0 1.5c.8 0 1.8 1.9 2 4.7H6c.2-2.8 1.2-4.7 2-4.7zM2.6 8.8H4.6c.1 1.6.4 3 .9 4A5.5 5.5 0 0 1 2.6 8.8zm0-1.6A5.5 5.5 0 0 1 5.5 3.2c-.5 1-.8 2.4-.9 4zM6 8.8h4c-.2 2.8-1.2 4.7-2 4.7s-1.8-1.9-2-4.7zm5.4 0h2a5.5 5.5 0 0 1-2.9 4c.5-1 .8-2.4.9-4zm0-1.6c-.1-1.6-.4-3-.9-4a5.5 5.5 0 0 1 2.9 4z"/></svg>
        <span>www.crestwa.com</span>
      </li>
    </ul>

    <div class="base-band"></div>
  </div>
</body>
</html>
```